Business Card Design, including supply of raw art files plus a vector diagram of the zelvon logo and

We need the business card design for a company that is launching a new exciting product. The brief requires the submission of the following once the final design is chosen:

- business card layout including raw files
- a composite vector image file of the zelvon logo and tag line
- a standalone vector image file of the zelvon logo

The product will be launched as a customer engagement app.

It has 4 core modules which enables a person to do multiple things - book tours and activities, order takeaways, search for local deals and offers. A universal currency is at the heart of this product. When you use the app, you earn cashback rewards when shopping or buying at any of the merchant partners across the modules as . These rewards can then be used as full or part payment when buying goods or services at these merchant partners.

The business card must help us build the brand, communicate the benefit of the brand's key focus - the ability to earn and burn this universal cashback ccurrency - across the 4 modules - booking of tours and activities, ordering, searching for local deals and payment.

We would like the design to use the brand's blue colour the hex colour is: 00
Dark grey : 646464
Darker blue shadow: 058bdd
Main Blue: 0084ff

We need to translate this into a CMYK print or spot colour print.

Both print options to be supplied as separate files.

An example of the base concept we have in mind is attached for your reference.

The font used by the brand is Proxima Nova.

Note: the duration has been set as 2 days.

Industry/Entity Type

Business

Contact Information for Business Card

Carla Mendoza
Marketing
W: www.zelvon.example
M: + 61 400555123
T: +61 2 5550 1473
A: Suite 7, Level 2, 14-18 Harwick Street, Sydney, NSW, 2000, Australia

Font styles to use
Sans Serif

Requirements
Must have
• zelVon logo and tagline
• address details
• zelVon icons as supplied
Nice to have
• would like to have the option of a spot varnish layer over the logo and icons at the back of the card

```html
<!DOCTYPE html>
<html lang="en">
<head>
<meta charset="utf-8">
<title>zelVon business card</title>
<link rel="stylesheet" href="https://fonts.googleapis.com/css2?family=Roboto:wght@300;400;700&display=swap">
<style>
  :root {
    --brand-blue: #0a86d8;
    --brand-blue-deep: #058bdd;
    --text-grey: #646464;
    --card-white: #ffffff;
    --backdrop: #e9ebee;
  }
  * { box-sizing: border-box; margin: 0; padding: 0; }
  html, body {
    width: 1200px; height: 900px; overflow: hidden;
    background: var(--backdrop);
    font-family: "Roboto", Arial, sans-serif;
  }
  .stage { position: relative; width: 1200px; height: 900px; }
  .card {
    position: absolute; left: 280px; width: 640px; height: 366px;
    overflow: hidden;
    box-shadow: 0 6px 18px rgba(0,0,0,.18);
  }
  .card--front { top: 46px; background: var(--brand-blue); color: var(--card-white); }
  .card--back { top: 448px; background: var(--card-white); color: var(--text-grey); }

  /* brand name block */
  .brand { position: absolute; }
  .brand__name { font-weight: 400; line-height: 1; display: block; }
  .brand__tagline { font-weight: 300; display: block; white-space: nowrap; }

  .card--front .brand { left: 0; right: 0; top: 84px; text-align: center; }
  .card--front .brand__name { font-size: 72px; }
  .card--front .brand__tagline { font-size: 22px; margin-top: 12px; }

  .modules {
    position: absolute; left: 110px; right: 70px; top: 246px;
    display: flex; justify-content: space-between;
    list-style: none;
  }
  .module { width: 110px; text-align: center; font-size: 11px; font-weight: 400; }
  .module svg { display: block; margin: 0 auto 8px; height: 32px; }

  .card--back .brand { left: 40px; top: 40px; }
  .card--back .brand__name { font-size: 44px; color: var(--text-grey); }
  .card--back .brand__tagline { font-size: 15px; margin-top: 6px; color: var(--text-grey); }

  .contact { position: absolute; left: 66px; top: 150px; font-size: 15px; line-height: 21px; font-style: normal; }
  .contact__address { margin-bottom: 6px; padding-left: 10px; }
  .contact__list { list-style: none; }
  .contact__list li { display: flex; align-items: center; }
  .contact__list svg { width: 12px; height: 12px; margin-right: 6px; flex: none; }

  .person { position: absolute; right: 60px; top: 190px; text-align: right; }
  .person__name { font-size: 22px; font-weight: 700; color: var(--brand-blue); }
  .person__role { font-size: 16px; font-weight: 300; }
  .side-tab {
    position: absolute; right: 0; top: 226px; width: 12px; height: 36px;
    background: var(--brand-blue-deep); border-radius: 6px 0 0 6px;
  }
</style>
</head>
<body>
<main class="stage">

  <section class="card card--front" aria-label="Card front">
    <div class="brand">
      <span class="brand__name">zelVon</span>
      <span class="brand__tagline">earn it, spend it</span>
    </div>
    <ul class="modules">
      <li class="module">
        <svg viewBox="0 0 32 32" width="32" fill="none" stroke="#fff" stroke-width="2.4">
          <path d="M6 13a10 10 0 0 1 18-4"/><path d="M24 4v5h-5"/>
          <path d="M26 19a10 10 0 0 1-18 4"/><path d="M8 28v-5h5"/>
          <path d="M18.5 12.5c-1-1-5-1.2-5 1s5 1.4 5 3.6-4 2-5 .8M16 10.5v11" stroke-width="1.8"/>
        </svg>
        CashBack Rewards
      </li>
      <li class="module">
        <svg viewBox="0 0 40 32" width="40" fill="#fff">
          <path d="M4 8h8l3-4h10l3 4h8v20H4z"/>
          <circle cx="20" cy="17" r="7" fill="var(--brand-blue)"/>
          <circle cx="20" cy="17" r="4.5"/>
        </svg>
        Tours &amp; Activities
      </li>
      <li class="module">
        <svg viewBox="0 0 32 32" width="32" fill="none" stroke="#fff" stroke-width="2.4" stroke-linecap="round">
          <path d="M6 4l20 24"/><path d="M26 4L6 28"/>
          <path d="M22 3l6 6M20 5l3 3"/>
        </svg>
        Mobile Ordering
      </li>
      <li class="module">
        <svg viewBox="0 0 36 32" width="36" fill="#fff">
          <path d="M4 14L18 4h14v14L18 28z"/>
          <circle cx="27" cy="9" r="2.2" fill="var(--brand-blue)"/>
        </svg>
        Local Offers
      </li>
    </ul>
  </section>

  <section class="card card--back" aria-label="Card back">
    <div class="brand">
      <span class="brand__name">zelVon</span>
      <span class="brand__tagline">earn it, spend it</span>
    </div>

    <address class="contact">
      <p class="contact__address">Suite 7, Level 2, 14-18 Harwick<br>Street, Sydney NSW 2000</p>
      <ul class="contact__list">
        <li><svg viewBox="0 0 12 12"><rect x="3" y="0.5" width="6" height="11" rx="1" fill="var(--brand-blue)"/><rect x="4" y="2" width="4" height="7" fill="#fff"/></svg>+61 400 555 123</li>
        <li><svg viewBox="0 0 12 12"><path d="M2 1l3 1-1 3c1 2 2 3 3 3l3-1 1 3-2 1C5 11 1 7 1 3z" fill="var(--brand-blue)"/></svg>+61 2 5550 1473</li>
        <li><svg viewBox="0 0 12 12" fill="var(--brand-blue)"><rect x="3" y="1" width="6" height="3"/><rect x="1" y="4" width="10" height="5" rx="1"/><rect x="3" y="8" width="6" height="3" fill="#fff" stroke="var(--brand-blue)"/></svg>+61 2 5550 1480</li>
        <li><svg viewBox="0 0 12 12"><rect x="0.5" y="2" width="11" height="8" fill="var(--brand-blue)"/><path d="M1 2.5l5 4 5-4" fill="none" stroke="#fff"/></svg>carla.mendoza@zelvon.example</li>
        <li><svg viewBox="0 0 12 12" fill="none" stroke="var(--brand-blue)"><circle cx="6" cy="6" r="5"/><path d="M1 6h10M6 1c-3 3-3 7 0 10M6 1c3 3 3 7 0 10"/></svg>www.zelvon.example</li>
      </ul>
    </address>

    <div class="person">
      <p class="person__name">Carla Mendoza</p>
      <p class="person__role">Marketing</p>
    </div>
    <span class="side-tab" aria-hidden="true"></span>
  </section>

</main>
</body>
</html>
```